Business Card design for new private practice opening

I need a business card design for my new private practice with my new logo uploaded as a file
On the front the logo
On the back: maybe a small logo somewhere?
Priv. Doz. DDr. Corinna Vestaluk
Fachärztin für Allgemein- & Viszeralchirurgie
Address: xxx
Tel: xxx
Mobil:xxx
Webseite:xxx
Email:xxx

Contact Information for Business Card

See project description above for details

Requirements
Nice to have
• I would like the colors of the logo incorporated into the business card

```html
<!DOCTYPE html>
<html lang="de">
<head>
<meta charset="utf-8">
<title>Vestaluk Chirurgie – Visitenkarte</title>
<link rel="stylesheet" href="https://fonts.googleapis.com/css2?family=Montserrat:wght@400;500;700&display=swap">
<style>
  :root {
    --teal: #45b8b4;
    --grey: #858585;
    --ring-grey: #7f7f7f;
    --faint-grey: #ededed;
    --divider: #eef0f0;
    --card: #ffffff;
    --backdrop: #eeeeee;
  }
  * { margin: 0; padding: 0; box-sizing: border-box; }
  html, body { width: 1200px; height: 1200px; overflow: hidden; }
  body {
    background: var(--backdrop);
    font-family: "Montserrat", Arial, sans-serif;
    position: relative;
  }
  .card {
    position: absolute;
    left: 202px;
    width: 796px;
    height: 456px;
    background: var(--card);
    overflow: hidden;
  }
  .card--front { top: 120px; }
  .card--back { top: 624px; }

  /* Front */
  .front-panel-divider {
    position: absolute; left: 530px; top: 0; width: 2px; height: 100%;
    background: var(--divider);
  }
  .front-decor-ring {
    position: absolute; left: 464px; top: 0;
    width: 456px; height: 456px;
  }
  .brand {
    position: absolute; left: 168px; top: 166px;
    display: flex; align-items: center; gap: 30px;
  }
  .brand-mark {
    width: 124px; height: 124px; border-radius: 50%;
    border: 7px solid var(--ring-grey);
    flex: none;
  }
  .brand-name {
    color: var(--grey); font-weight: 700;
    font-size: 54px; line-height: 1.02; letter-spacing: 0.5px;
  }

  /* Back */
  .holder-name {
    position: absolute; left: 52px; top: 46px;
    color: var(--teal); font-weight: 500; font-size: 34px; letter-spacing: 0.3px;
  }
  .holder-title {
    position: absolute; left: 53px; top: 92px;
    color: var(--grey); font-size: 18.5px; letter-spacing: 0.6px;
    text-transform: uppercase;
  }
  .name-rule {
    position: absolute; left: 53px; top: 120px; width: 677px; height: 3px;
    background: linear-gradient(90deg, var(--teal) 0%, var(--teal) 45%, rgba(133,133,133,0.4) 100%);
    border-radius: 2px;
  }
  .contact-list {
    position: absolute; left: 50px; top: 142px; list-style: none;
  }
  .contact-item {
    display: flex; align-items: center; height: 47.3px;
    color: var(--grey); font-size: 28px; letter-spacing: 0.4px;
  }
  .contact-icon {
    width: 22px; height: 22px; margin-right: 17px; fill: var(--teal); flex: none;
  }
  .back-brand {
    position: absolute; right: 58px; bottom: 56px;
    display: flex; align-items: center; gap: 14px;
  }
  .back-brand .brand-mark {
    width: 132px; height: 132px; border-width: 6px;
  }
  .back-brand-name {
    color: var(--grey); font-weight: 700; font-size: 15px; line-height: 1.15;
    position: absolute; right: 0; top: 142px; white-space: nowrap; text-align: right;
  }
</style>
</head>
<body>

<section class="card card--front" aria-label="Vorderseite">
  <div class="front-panel-divider"></div>
  <svg class="front-decor-ring" viewBox="0 0 456 456" aria-hidden="true">
    <circle cx="228" cy="228" r="220" fill="none" stroke="#ededed" stroke-width="12"/>
  </svg>
  <div class="brand">
    <div class="brand-mark" aria-hidden="true"></div>
    <div class="brand-name">VESTALUK<br>CHIRURGIE</div>
  </div>
</section>

<section class="card card--back" aria-label="Rückseite">
  <h1 class="holder-name">Priv. Doz. DDr. Corinna Vestaluk</h1>
  <p class="holder-title">Fachärztin für Allgemein- &amp; Viszeralchirurgie</p>
  <div class="name-rule"></div>

  <ul class="contact-list">
    <li class="contact-item">
      <svg class="contact-icon" viewBox="0 0 24 24" aria-hidden="true"><path d="M12 1.5a7.5 7.5 0 0 0-7.5 7.5c0 5.6 7.5 13.5 7.5 13.5s7.5-7.9 7.5-13.5A7.5 7.5 0 0 0 12 1.5zm0 10.3a2.8 2.8 0 1 1 0-5.6 2.8 2.8 0 0 1 0 5.6z"/></svg>
      Address: xxx
    </li>
    <li class="contact-item">
      <svg class="contact-icon" viewBox="0 0 24 24" aria-hidden="true"><path d="M6.6 2.5l3 3.6c.4.5.4 1.2 0 1.7L8 9.7c1.3 2.6 3.5 4.9 6.2 6.3l1.9-1.6c.5-.4 1.2-.4 1.7 0l3.6 3c.5.4.6 1.2.1 1.7l-2 2.2c-.6.6-1.5.9-2.3.7C9.6 20.4 3.6 14.4 2 6.8c-.2-.8.1-1.7.7-2.3l2.2-2c.5-.5 1.3-.4 1.7 0z"/></svg>
      Tel: xxx
    </li>
    <li class="contact-item">
      <svg class="contact-icon" viewBox="0 0 24 24" aria-hidden="true"><path d="M7.5 1h9A1.5 1.5 0 0 1 18 2.5v19a1.5 1.5 0 0 1-1.5 1.5h-9A1.5 1.5 0 0 1 6 21.5v-19A1.5 1.5 0 0 1 7.5 1zm3.5 18.5v1.5h2v-1.5z"/></svg>
      Mobil: xxx
    </li>
    <li class="contact-item">
      <svg class="contact-icon" viewBox="0 0 24 24" aria-hidden="true"><path d="M12 2a10 10 0 1 0 0 20 10 10 0 0 0 0-20zm6.9 9h-3a15 15 0 0 0-1.2-5.6A8 8 0 0 1 18.9 11zM12 4.1c.9 1.2 1.7 3.6 1.9 6.9h-3.8c.2-3.3 1-5.7 1.9-6.9zM9.3 5.4A15 15 0 0 0 8.1 11h-3a8 8 0 0 1 4.2-5.6zM5.1 13h3a15 15 0 0 0 1.2 5.6A8 8 0 0 1 5.1 13zm6.9 6.9c-.9-1.2-1.7-3.6-1.9-6.9h3.8c-.2 3.3-1 5.7-1.9 6.9zm2.7-1.3a15 15 0 0 0 1.2-5.6h3a8 8 0 0 1-4.2 5.6z"/></svg>
      Webseite: xxx
    </li>
    <li class="contact-item">
      <svg class="contact-icon" viewBox="0 0 24 24" aria-hidden="true"><path d="M2 5.5A1.5 1.5 0 0 1 3.5 4h17A1.5 1.5 0 0 1 22 5.5v.6l-10 6.3L2 6.1zm0 3l10 6.2 10-6.2v10A1.5 1.5 0 0 1 20.5 20h-17A1.5 1.5 0 0 1 2 18.5z"/></svg>
      Email: xxx
    </li>
  </ul>

  <div class="back-brand">
    <div class="brand-mark" aria-hidden="true"></div>
    <div class="back-brand-name">VESTALUK CHIRURGIE</div>
  </div>
</section>

</body>
</html>
```